Stationery design for law/Property/finance business

We need stationery design for a Law/Property/Finance business called Ridgemoor. Logo is attached.
we require a letterhead and with compliments slip.
Would like to see a very simple professional design using the colours of the logo and offset against Charcoal colours. Maybe a charcoal band for header and footer with logo and details appearing in it? Former letterhead attached for examples.
we require the project to be provided in word, pdf and jpeg format.
we require the following details on the stationery:
Cairns Phone: 07 40551926
Weipa Phone: 07 40613847
Mobile: 0491 570 384
Fax: 07 40338172
email: admin@ridgemoorholdings-example.com.au
ABN 51 824 306 917

```html
<!DOCTYPE html>
<html lang="en">
<head>
<meta charset="utf-8">
<title>Ridgemoor Stationery</title>
<link rel="stylesheet" href="https://fonts.googleapis.com/css2?family=Roboto:wght@400;700&display=swap">
<style>
  :root {
    --board: #5c4c43;
    --paper: #ffffff;
    --brand-blue: #2b9ad6;
    --band-blue: #1f9ad8;
    --charcoal: #6b6b70;
    --ink: #6e6e72;
    --ink-strong: #55555a;
    --ghost: #eef1f7;
    --abn: #0d5f94;
    --corner-tint: #e3ecf6;
  }
  * { margin: 0; padding: 0; box-sizing: border-box; }
  html, body { width: 1200px; height: 770px; overflow: hidden; }
  body {
    position: relative;
    background: var(--board);
    font-family: "Roboto", Arial, sans-serif;
  }
  .sheet {
    position: absolute;
    background: var(--paper);
    box-shadow: 2px 3px 4px rgba(0,0,0,.35);
    overflow: hidden;
  }
  .letterhead { left: 62px; top: 79px; width: 489px; height: 633px; }
  .comp-slip { left: 581px; top: 499px; width: 474px; height: 213px; }

  .brand-name {
    position: absolute;
    font-weight: 700;
    color: var(--brand-blue);
    letter-spacing: .01em;
    line-height: 1;
    display: flex;
    align-items: center;
    gap: 6px;
  }
  .brand-name .mark-dot {
    display: inline-block;
    border-radius: 50%;
    background: var(--brand-blue);
  }
  .letterhead .brand-name { left: 28px; top: 54px; font-size: 20px; }
  .letterhead .brand-name .mark-dot { width: 9px; height: 9px; }
  .comp-slip .brand-name { left: 25px; top: 46px; font-size: 18px; }
  .comp-slip .brand-name .mark-dot { width: 8px; height: 8px; }

  .feature-name {
    position: absolute;
    left: 612px; top: 152px;
    font-size: 46px; font-weight: 700;
    color: var(--brand-blue);
    display: flex; align-items: center; gap: 12px;
    line-height: 1;
  }
  .feature-name .mark-dot { width: 18px; height: 18px; border-radius: 50%; background: var(--brand-blue); }

  .ghost-name {
    position: absolute;
    font-weight: 700;
    color: var(--ghost);
    line-height: 1;
    white-space: nowrap;
  }
  .letterhead .ghost-name { left: 90px; top: 418px; font-size: 52px; }
  .comp-slip .ghost-name { left: 355px; top: 38px; font-size: 19px; }

  .corner-accent {
    position: absolute;
    left: 424px; top: 138px;
    width: 38px; height: 38px;
    border-radius: 50%;
    background: var(--corner-tint);
  }

  .contact-line {
    position: absolute;
    font-size: 7.5px;
    color: var(--ink);
    white-space: nowrap;
    display: flex;
    align-items: center;
  }
  .contact-line b { color: var(--ink-strong); font-weight: 700; }
  .contact-line .sep {
    display: inline-block; width: 1px; height: 9px;
    background: var(--ink-strong); margin: 0 7px;
  }
  .letterhead .contact-line { left: 21px; top: 583px; }
  .comp-slip .contact-line { left: 29px; top: 167px; }

  .footer-band {
    position: absolute;
    right: 0;
    display: flex;
    height: 18px;
    font-size: 7.2px;
    color: #fff;
    white-space: nowrap;
  }
  .footer-band .band-label {
    background: var(--charcoal);
    border-radius: 9px 0 0 9px;
    font-weight: 700;
    display: flex; align-items: center;
    padding-left: 11px;
    margin-right: -9px;
  }
  .footer-band .band-contact {
    flex: 1;
    background: var(--band-blue);
    border-radius: 9px 0 0 9px;
    display: flex; align-items: center;
    padding-left: 13px;
    gap: 8px;
  }
  .footer-band .band-square { width: 6px; height: 6px; background: #6a7a86; flex: none; }
  .footer-band .abn { color: var(--abn); font-weight: 700; }
  .letterhead .footer-band { top: 598px; left: 12px; }
  .letterhead .band-label { width: 203px; }
  .comp-slip .footer-band { top: 182px; left: 21px; height: 17px; }
  .comp-slip .band-label { width: 181px; }
</style>
</head>
<body>

  <section class="sheet letterhead" aria-label="Letterhead">
    <div class="brand-name"><span>RIDGEMOOR</span><span class="mark-dot"></span></div>
    <div class="ghost-name" aria-hidden="true">RIDGEMOOR</div>
    <p class="contact-line">
      <b>Cairns Phone:</b>&nbsp;07 40551926<span class="sep"></span>
      <b>Weipa Phone:</b>&nbsp;07 40613847<span class="sep"></span>
      <b>Mobile:</b>&nbsp;0491 570 384<span class="sep"></span>
      <b>Fax:</b>&nbsp;07 40338172
    </p>
    <div class="footer-band">
      <div class="band-label">Law/Property/Finance business Ridgemoor</div>
      <div class="band-contact">
        <span>email: admin@ridgemoorholdings-example.com.au</span>
        <span class="band-square"></span>
        <span class="abn">ABN 51 824 306 917</span>
      </div>
    </div>
  </section>

  <div class="feature-name"><span>RIDGEMOOR</span><span class="mark-dot"></span></div>

  <section class="sheet comp-slip" aria-label="With compliments slip">
    <div class="brand-name"><span>RIDGEMOOR</span><span class="mark-dot"></span></div>
    <div class="ghost-name" aria-hidden="true">RIDGEMOOR</div>
    <div class="corner-accent" aria-hidden="true"></div>
    <p class="contact-line">
      <b>Cairns Phone:</b>&nbsp;07 40551926<span class="sep"></span>
      <b>Weipa Phone:</b>&nbsp;07 40613847<span class="sep"></span>
      <b>Mobile:</b>&nbsp;0491 570 384<span class="sep"></span>
      <b>Fax:</b>&nbsp;07 40338172
    </p>
    <div class="footer-band">
      <div class="band-label">Law/Property/Finance business Ridgemoor</div>
      <div class="band-contact">
        <span>email: admin@ridgemoorholdings-example.com.au</span>
        <span class="band-square"></span>
        <span class="abn">ABN 51 824 306 917</span>
      </div>
    </div>
  </section>

</body>
</html>
```